Personal Business card and maybe logo or graphic?

I would like a card to give out like you would a business card, however I am not promoting a business, it is just for my personal details.

I have no brand and no logo to worry about.

I would like some images or a logo of some kind or a graphic so the card has some excitement about it.

I am happy if you wish to create a logo/graphic that represents my name, I have seen someone with just their initials as a graphic so for me PH, however I am happy for you to create anything you wish, it does not have to relate to me just make the card look fun and still professional.

Please use the details

Peter Hadley

Ashcombe Lodge
9 The Mews
Fern Close
Bournemouth
Dorset
BH4 2QT

+44 (0)7812 604258
peter@hadleypost.example
linkedin.example/in/hadleypeter

looking for a mix between fun, fresh , young whilst being professional

I am new to this and am looking for you to guide me through the process please ask questions and ideas

I am just tidying up my brief as I am starting to understand more. hope it has not confused anyone
Updates

Reason: I have not had time to review or comment due to personal issues sorry

Hi,

to help would you be so kind as to use these sample details on the card

I am uk based and a few designs have us details which look different

Peter Hadley

Ashcombe lodge

9 The Mews

Fern Close

Bournemouth

Dorset

BH4 2QT

+44 (0)7812 604258

peter@hadleypost.example

many thanks hope that is ok and not too much trouble!

regards

Pim

My are of expertise is IT management / IT Consultancy, incase you wish to incorporate any graphics

My job was that of CIO (Chief Information Officer) or another term is Head of IT

just advising incase this gives any assistance as one designer has asked s may be useful to others

thanks                                   

just thought I have had a look and the UK size for a business card seems to be as per below

I thought I would mention as I guess the US size may be different and other countries too

I found these sizes on Cardforge but guess most companies will be similar

that said maybe you can advise me

I have no idea what cardforge is like so not sure where to get cards made, will figure that out later I guess but I assume dimensions are important for the design

thanks

 

Document Trim Size    

            Horizontal        

        85 x 55 mm           

1004 x 650 pixels           

            Vertical        

        55 x 85 mm           

650 x 1004 pixels           

        Full Bleed Size    

            Horizontal        

        88 x 58 mm           

1039 x 685 pixels           

            Vertical        

        58 x 88 mm           

685 x 1039 pixels           

 many thanks

Target Market(s)

Professional and personal contacts

Industry/Entity Type

Business

```html
<!DOCTYPE html>
<html lang="en">
<head>
<meta charset="utf-8">
<title>Peter Hadley – Personal Card Concepts</title>
<link rel="stylesheet" href="https://fonts.googleapis.com/css2?family=Lobster&family=Kaushan+Script&family=Open+Sans:wght@400;500&family=Arimo:wght@700&family=Tinos&display=swap">
<style>
  :root {
    --paper: #ffffff;
    --ink: #000000;
    --band: #000000;
    --band-grey: #a6a6a6;
    --ghost: #cfcfcf;
    --edge: #9a9a9a;
  }
  * { margin: 0; padding: 0; box-sizing: border-box; }
  html, body {
    width: 1200px; height: 892px; overflow: hidden;
    background: var(--paper);
  }
  .sheet { position: relative; width: 1200px; height: 892px; }
  .card {
    position: absolute;
    background: var(--paper);
    border: 1px solid var(--edge);
    overflow: hidden;
    color: var(--ink);
  }

  /* Card 1 – landscape, black band */
  .card--band { left: 17px; top: 17px; width: 648px; height: 406px; }
  .card--band .band-art { position: absolute; left: 0; top: 0; }
  .card--band .name {
    position: absolute; left: 24px; top: 26px;
    font: 84px/1 "Lobster", cursive;
    color: var(--paper); white-space: nowrap;
  }
  .card--band .address {
    position: absolute; left: 39px; top: 158px;
    font: 700 21px/38px "Arimo", sans-serif;
    list-style: none;
  }
  .card--band .contact {
    position: absolute; right: 22px; top: 262px;
    font: 20px/37px "Tinos", serif;
    text-align: right; list-style: none;
  }

  /* Card 2 – portrait, stacked name */
  .card--stack { left: 698px; top: 14px; width: 488px; height: 810px; }
  .card--stack .name-block {
    position: absolute; left: 22px; top: 25px; width: 447px; height: 299px;
    background: var(--band); color: var(--paper);
    text-align: center; font-family: "Open Sans", sans-serif;
  }
  .card--stack .first {
    display: block; font-size: 158px; line-height: 1; margin-top: 10px;
    letter-spacing: -2px;
  }
  .card--stack .last {
    display: block; font-size: 92px; line-height: 1; margin-top: 4px;
  }
  .card--stack .address {
    position: absolute; left: 0; right: 0; top: 352px;
    font: 500 28px/40px "Open Sans", sans-serif;
    text-align: center; list-style: none;
  }
  .card--stack .contact {
    position: absolute; left: 0; right: 0; top: 632px;
    font: 24px/37px "Open Sans", sans-serif;
    text-align: center; list-style: none;
  }

  /* Card 3 – landscape, script with ghosted name */
  .card--script { left: 17px; top: 479px; width: 648px; height: 395px; }
  .card--script .ghost-name {
    position: absolute; left: 18px; top: 18px;
    font: 94px/1 "Kaushan Script", cursive;
    color: var(--ghost); white-space: nowrap;
  }
  .card--script .name {
    position: absolute; right: 30px; top: 96px;
    font: 42px/1 "Kaushan Script", cursive;
  }
  .card--script .address {
    position: absolute; left: 34px; top: 162px;
    font: 26px/35px "Kaushan Script", cursive;
    list-style: none;
  }
  .card--script .contact {
    position: absolute; right: 30px; top: 258px;
    font: 23px/36px "Kaushan Script", cursive;
    text-align: right; list-style: none;
  }
</style>
</head>
<body>
<main class="sheet">

  <section class="card card--band">
    <svg class="band-art" width="648" height="406" viewBox="0 0 648 406" aria-hidden="true">
      <polygon points="430,8 646,8 646,44 470,44" fill="var(--band-grey)"/>
      <polygon points="0,24 536,24 508,124 0,124" fill="var(--band)"/>
      <polygon points="520,60 630,60 620,92 510,92" fill="var(--band-grey)"/>
    </svg>
    <h1 class="name">Peter Hadley</h1>
    <ul class="address">
      <li>Ashcombe Lodge</li>
      <li>9 The Mews</li>
      <li>Fern Close</li>
      <li>Bournemouth, Dorset</li>
      <li>BH4 2QT</li>
    </ul>
    <ul class="contact">
      <li>+44 (0)7812 604258</li>
      <li>peter@hadleypost.example</li>
      <li>linkedin.example/in/hadleypeter</li>
    </ul>
  </section>

  <section class="card card--stack">
    <h1 class="name-block">
      <span class="first">Peter</span>
      <span class="last">Hadley</span>
    </h1>
    <ul class="address">
      <li>Ashcombe Lodge</li>
      <li>9 The Mews</li>
      <li>Fern Close</li>
      <li>Bournemouth, Dorset</li>
      <li>BH4 2QT</li>
    </ul>
    <ul class="contact">
      <li>+44 (0)7812 604258</li>
      <li>peter@hadleypost.example</li>
      <li>linkedin.example/in/hadleypeter</li>
    </ul>
  </section>

  <section class="card card--script">
    <p class="ghost-name" aria-hidden="true">Peter Hadley</p>
    <h1 class="name">Peter Hadley</h1>
    <ul class="address">
      <li>Ashcombe Lodge</li>
      <li>9 The Mews</li>
      <li>Fern Close</li>
      <li>Bournemouth, Dorset</li>
      <li>BH4 2QT</li>
    </ul>
    <ul class="contact">
      <li>+44 (0)7812 604258</li>
      <li>peter@hadleypost.example</li>
      <li>linkedin.example/in/hadleypeter</li>
    </ul>
  </section>

</main>
</body>
</html>
```